Create a bold and border around my logo to make it pop and sign graphic design

I would like someone to create a sign graphic design so I can use on the side of my trucks and put on yard signs. I would to remove a lot of the white and add more of the orange and blue to give it more pop when cars drive past. I would like the services to be removed and for you to leave space for a mobile number that i would add later. I don’t want my logo changed at all. I just want colour and design to be added to the background so i can use it in signage. Same colour as on the sign

```html
<!DOCTYPE html>
<html lang="en">
<head>
<meta charset="utf-8">
<title>Branchworthy Vehicle Sign</title>
<link href="https://fonts.googleapis.com/css2?family=Anton&display=swap" rel="stylesheet">
<style>
  :root {
    --page-bg: #ffffff;
    --brand-orange: #d55220;
    --brand-blue: #053a86;
    --mid-plum: #5b4356;
    --glow: rgba(225, 222, 235, 0.95);
    --frame-line: rgba(255, 255, 255, 0.45);
    --text-white: #ffffff;
    --text-shadow: rgba(20, 15, 30, 0.75);
  }
  * { margin: 0; padding: 0; box-sizing: border-box; }
  html, body {
    width: 1200px;
    height: 1000px;
    overflow: hidden;
    background: var(--page-bg);
  }
  .canvas {
    position: relative;
    width: 1200px;
    height: 1000px;
  }
  .sign {
    position: absolute;
    left: 22px;
    top: 229px;
    width: 1156px;
    height: 540px;
    overflow: hidden;
    background: linear-gradient(100deg,
      var(--brand-orange) 0%,
      #c24f26 22%,
      var(--mid-plum) 45%,
      #253a6e 65%,
      var(--brand-blue) 85%,
      #073b85 100%);
  }
  .sign__glow {
    position: absolute;
    left: 398px;
    top: 22px;
    width: 360px;
    height: 300px;
    background: radial-gradient(ellipse at center,
      var(--glow) 0%,
      rgba(200, 195, 215, 0.6) 30%,
      rgba(150, 130, 160, 0.2) 58%,
      rgba(120, 100, 130, 0) 75%);
  }
  .sign__frame {
    position: absolute;
    left: 14px;
    top: 14px;
    right: 14px;
    bottom: 14px;
    border: 1.5px solid var(--frame-line);
  }
  .brand-mark {
    position: absolute;
    left: 0;
    right: 0;
    top: 145px;
    display: flex;
    align-items: center;
    justify-content: center;
    gap: 14px;
    font-family: 'Anton', 'Impact', sans-serif;
    font-size: 40px;
    color: var(--brand-blue);
    letter-spacing: 1px;
  }
  .brand-mark__dot {
    width: 34px;
    height: 34px;
    border-radius: 50%;
    background: var(--brand-orange);
  }
  .sign__name,
  .sign__phone {
    position: absolute;
    left: 0;
    right: 0;
    text-align: center;
    font-family: 'Anton', 'Impact', sans-serif;
    color: var(--text-white);
    text-shadow: 4px 5px 4px var(--text-shadow);
    line-height: 1;
  }
  .sign__name {
    top: 292px;
    font-size: 104px;
    letter-spacing: 1px;
  }
  .sign__phone {
    top: 412px;
    font-size: 84px;
    letter-spacing: 0.5px;
  }
</style>
</head>
<body>
  <div class="canvas">
    <section class="sign">
      <div class="sign__glow"></div>
      <div class="sign__frame"></div>
      <div class="brand-mark">
        <span class="brand-mark__dot"></span>
        <span class="brand-mark__name">BRANCHWORTHY</span>
      </div>
      <h1 class="sign__name">BRANCHWORTHY</h1>
      <p class="sign__phone">Call: 044-987 654 321</p>
    </section>
  </div>
</body>
</html>
```